LEARN Business Skills so you can Earn a good living

size of the poster is 8”x 10.75" plus 0.25" bleed.
Please leave 1 inch on the bottoum for footer
I want a design a poster that will attract people's attention.
I appreciate a creative ad however the ad should not take away from being able to clearly read the text.
-I also appreciate a simple creative ad that is not too busy.
-you can use graphics, vectors, or pictures of real people.
-however, if you use real people it should be a white male that is wearing a white shirt and look like a professional person.

Target Market(s)

Potential young business people

Industry/Entity Type

education

Requirements
Must have
• easy to read the text
Nice to have
• I would like a "creative" simple ad that is easy to be read
Should not have
• pictures of women

```html
<!DOCTYPE html>
<html lang="en">
<head>
<meta charset="utf-8">
<title>Learn It to Earn It – Business Enrichment Course</title>
<link rel="stylesheet" href="https://fonts.googleapis.com/css2?family=Montserrat:wght@400;700;800;900&family=Dancing+Script:wght@600&display=swap">
<style>
  :root {
    --page-bg: #e9e9ea;
    --ink: #403e50;
    --sky-top: #cbcfd2;
    --sky-bottom: #d3d6d8;
    --wall-light: #dcdcdc;
    --wall-mid: #c9c9c9;
    --ghost: rgba(255,255,255,0.42);
    --divider: #8d8f99;
    --footer: #ffffff;
  }
  * { margin: 0; padding: 0; box-sizing: border-box; }
  html, body { width: 1200px; height: 1200px; overflow: hidden; background: var(--page-bg); }
  .poster {
    position: absolute; left: 209px; top: 81px;
    width: 782px; height: 1035px; overflow: hidden;
    background: linear-gradient(180deg, var(--sky-top) 0%, var(--sky-bottom) 47%);
    font-family: "Montserrat", sans-serif; color: var(--ink);
  }
  .hero-photo {
    position: absolute; left: 0; top: 487px; width: 782px; height: 455px;
    background:
      radial-gradient(ellipse 240px 320px at 290px 320px, #ececec 0%, rgba(236,236,236,0) 70%),
      linear-gradient(180deg, var(--wall-mid) 0%, var(--wall-light) 60%, #d2d2d2 100%);
  }
  .ghost-letters, .headline { position: absolute; left: 0; top: 0; width: 782px; height: 1035px; }
  .footer-space {
    position: absolute; left: 0; top: 942px; width: 782px; height: 93px;
    background: var(--footer);
  }
  .course-title {
    position: absolute; right: 429px; top: 318px; width: 320px;
    text-align: right; font-weight: 800; font-size: 41px; line-height: 42px; letter-spacing: -0.3px;
  }
  .course-tagline {
    position: absolute; right: 429px; top: 452px; width: 200px;
    text-align: right; font-weight: 400; font-size: 13px; line-height: 17.5px;
  }
  .divider {
    position: absolute; left: 391px; top: 312px; width: 1px; height: 183px; background: var(--divider);
  }
  .benefits-intro {
    position: absolute; left: 423px; top: 320px; font-size: 13px; font-weight: 400; white-space: nowrap;
  }
  .benefits {
    position: absolute; left: 424px; top: 339px; width: 285px;
    font-weight: 800; font-size: 24px; line-height: 36px; letter-spacing: -0.2px;
  }
  .topics {
    position: absolute; left: 424px; top: 568px; width: 292px;
    font-weight: 700; font-size: 8.7px; line-height: 15px; text-transform: uppercase; letter-spacing: -0.1px;
  }
</style>
</head>
<body>
<main class="poster">
  <div class="hero-photo" role="img" aria-label="Photo: smiling bearded young man in a white polo shirt pointing at himself and holding an open laptop, in front of a light grey wall"></div>

  <svg class="ghost-letters" viewBox="0 0 782 1035" aria-hidden="true">
    <g font-family="Montserrat, sans-serif" font-weight="800" fill="var(--ghost)" font-size="348">
      <text x="13" y="487" textLength="820" lengthAdjust="spacingAndGlyphs">ARN</text>
      <text x="13" y="788" textLength="820" lengthAdjust="spacingAndGlyphs">ARN</text>
    </g>
  </svg>

  <div class="footer-space"></div>

  <svg class="headline" viewBox="0 0 782 1035" role="img" aria-label="Learn it to earn it">
    <g font-family="Montserrat, sans-serif" font-weight="800" fill="var(--ink)" font-size="136">
      <text x="85" y="156" textLength="623" lengthAdjust="spacingAndGlyphs">LEARN IT</text>
      <text x="162" y="273" textLength="546" lengthAdjust="spacingAndGlyphs">EARN IT</text>
    </g>
    <text x="74" y="267" font-family="'Dancing Script', cursive" font-weight="600" font-size="80" fill="var(--ink)">to</text>
  </svg>

  <h1 class="course-title">Business Enrichment Course</h1>
  <p class="course-tagline">A proven success of helping people in their livelihoods</p>

  <div class="divider"></div>

  <p class="benefits-intro">Business skills that will help you:</p>
  <p class="benefits">Get a quality job - start / grow your business-Increase your salary</p>

  <p class="topics">Business Admiistration – Small Business Management - Finance - Investments - Computers- Accounting - Sales Marketing - Project Management Interviewing Skills - Business Law -Negotiation – Public Speaking - Import/Export - Information Technoloy -Distribution - Marketing - &nbsp;Ledgerly - Real Estate - Health Care-Management - Marketstall</p>
</main>
</body>
</html>
```